Revamp of business card

i need to revamp my business card to look more modern and neat

Contact Information for Business Card

details provided in pdf file, text will change

```html
<!DOCTYPE html>
<html lang="en">
<head>
<meta charset="utf-8">
<title>Inkora business card – front and back</title>
<link rel="stylesheet" href="https://fonts.googleapis.com/css2?family=Lato:wght@400;700;900&family=Montserrat:wght@700&display=swap">
<style>
  :root {
    --backdrop: #d3d3cf;
    --card: #ffffff;
    --accent: #e8482a;
    --ink: #2f2f2f;
    --muted: #5e5e5e;
    --dot-green: #e6efe9;
    --dot-peach: #fdeee2;
    --dot-blue: #e7ecf3;
    --dot-pink: #fbe7e9;
  }
  * { box-sizing: border-box; margin: 0; padding: 0; }
  html, body { width: 1200px; height: 801px; overflow: hidden; }
  body {
    background: var(--backdrop);
    font-family: "Lato", sans-serif;
    color: var(--ink);
    position: relative;
  }
  .card {
    position: absolute;
    top: 236px;
    width: 540px;
    height: 330px;
    background: var(--card);
    box-shadow: 0 6px 18px rgba(0,0,0,.18);
    overflow: hidden;
  }
  .card--front { left: 40px; }
  .card--back { left: 620px; }

  /* shared brand mark */
  .brand { display: flex; align-items: center; gap: 6px; color: var(--accent); font-weight: 900; }
  .brand__dot { border-radius: 50%; background: var(--accent); flex: none; }

  /* front */
  .front__brand { position: absolute; right: 34px; top: 40px; flex-direction: column; align-items: flex-end; gap: 2px; }
  .front__brand .brand__row { display: flex; align-items: center; gap: 8px; }
  .front__brand .brand__dot { width: 16px; height: 16px; }
  .front__brand .brand__name { font-size: 58px; line-height: 1; letter-spacing: -1px; }
  .front__tagline { font-size: 11px; color: var(--muted); font-weight: 400; }

  .front__marks { position: absolute; left: 30px; top: 34px; display: flex; align-items: flex-end; gap: 22px; }
  .front__marks .brand .brand__dot { width: 12px; height: 12px; }
  .front__marks .brand__name { font-size: 18px; }
  .social { display: flex; flex-direction: column; align-items: center; gap: 4px; }
  .social__dot { width: 34px; height: 34px; border-radius: 50%; background: var(--accent); }
  .social__handle { font-size: 9px; font-weight: 700; color: var(--ink); }

  .person { position: absolute; left: 30px; top: 168px; }
  .person__name { font-family: "Montserrat", sans-serif; font-weight: 700; font-size: 23px; color: var(--accent); letter-spacing: .5px; }
  .person__role { font-size: 14px; color: var(--muted); margin-top: 2px; }

  .contacts { position: absolute; left: 30px; top: 232px; list-style: none; }
  .contacts li { display: flex; align-items: center; gap: 10px; font-size: 13px; color: var(--ink); line-height: 20px; }
  .contacts svg { width: 13px; height: 13px; flex: none; }

  .address { position: absolute; right: 34px; bottom: 36px; text-align: right; font-size: 13px; line-height: 19px; color: var(--muted); }

  /* back */
  .back__dots span { position: absolute; border-radius: 50%; }
  .dot--green { width: 58px; height: 58px; left: 340px; top: 96px; background: var(--dot-green); }
  .dot--peach { width: 46px; height: 46px; left: 420px; top: 62px; background: var(--dot-peach); }
  .dot--blue { width: 72px; height: 72px; left: 300px; top: 156px; background: var(--dot-blue); }
  .dot--pink { width: 90px; height: 90px; left: 326px; top: 226px; background: var(--dot-pink); }

  .back__head { position: absolute; left: 28px; top: 30px; }
  .back__title { font-size: 36px; font-weight: 700; color: var(--accent); line-height: 1.05; }
  .back__subtitle { font-size: 15px; color: var(--ink); margin-top: 4px; }
  .back__links { font-size: 10.5px; color: var(--ink); margin-top: 6px; }

  .services { position: absolute; left: 28px; top: 168px; list-style: none; }
  .services li { margin-bottom: 10px; }
  .services h3 { font-size: 15px; font-weight: 700; color: var(--accent); line-height: 1.2; }
  .services p { font-size: 14px; color: var(--ink); line-height: 1.25; }

  .back__marks { position: absolute; right: 26px; bottom: 28px; display: grid; grid-template-columns: auto auto; gap: 12px 16px; align-items: end; justify-items: center; }
  .back__marks .social__dot { width: 28px; height: 28px; }
  .back__marks .social__handle { font-size: 8px; }
  .back__marks .brand .brand__dot { width: 10px; height: 10px; }
  .back__marks .brand__name { font-size: 16px; }
</style>
</head>
<body>

<section class="card card--front" aria-label="Business card front">
  <div class="brand front__brand">
    <div class="brand__row"><span class="brand__dot"></span><span class="brand__name">Inkora</span></div>
    <span class="front__tagline">where ink becomes art</span>
  </div>

  <div class="front__marks">
    <div class="brand"><span class="brand__dot"></span><span class="brand__name">Inkora</span></div>
    <div class="social"><span class="social__dot"></span><span class="social__handle">inkoraprints</span></div>
    <div class="social"><span class="social__dot"></span><span class="social__handle">inkora</span></div>
  </div>

  <div class="person">
    <h1 class="person__name">MARCUS DELANEY</h1>
    <p class="person__role">Director</p>
  </div>

  <ul class="contacts">
    <li>
      <svg viewBox="0 0 24 24" fill="none" stroke="#e8482a" stroke-width="2.4" stroke-linecap="round" stroke-linejoin="round"><path d="M5 3h4l2 5-3 2a12 12 0 0 0 6 6l2-3 5 2v4a2 2 0 0 1-2 2A18 18 0 0 1 3 5a2 2 0 0 1 2-2z"/></svg>
      0400 318 276
    </li>
    <li>
      <svg viewBox="0 0 24 24" fill="none" stroke="#e8482a" stroke-width="2.4" stroke-linejoin="round"><rect x="6" y="2" width="12" height="20" rx="2"/><line x1="10" y1="18" x2="14" y2="18"/></svg>
      08 7010 5523
    </li>
    <li>
      <svg viewBox="0 0 24 24" fill="none" stroke="#e8482a" stroke-width="2.4" stroke-linejoin="round"><rect x="2" y="5" width="20" height="14" rx="1"/><path d="M2 6l10 7 10-7"/></svg>
      marcus@inkora.com.au
    </li>
    <li>
      <svg viewBox="0 0 24 24" fill="none" stroke="#e8482a" stroke-width="2.2"><circle cx="12" cy="12" r="10"/><ellipse cx="12" cy="12" rx="4.5" ry="10"/><line x1="2" y1="12" x2="22" y2="12"/></svg>
      www.inkora.com.au
    </li>
  </ul>

  <address class="address" style="font-style:normal">
    Shop 4, 18 Harbour Lane,<br>
    Wattle Court Arcade, Riverton 5010
  </address>
</section>

<section class="card card--back" aria-label="Business card back">
  <div class="back__dots" aria-hidden="true">
    <span class="dot--peach"></span>
    <span class="dot--green"></span>
    <span class="dot--blue"></span>
    <span class="dot--pink"></span>
  </div>

  <div class="back__head">
    <h2 class="back__title">Art Prints &amp; Embroidery</h2>
    <p class="back__subtitle">Prints on all kinds of apparel fabrics</p>
    <p class="back__links">www.tevaro.com.au | www.bluethread.com.au | www.southwear.com.au | www.corbelapparel.com.au</p>
  </div>

  <ul class="services">
    <li>
      <h3>Prints on Promotional and Giveways</h3>
      <p>Mugs, Caps, KeyChains, Name Tags, Wall Clocks etc.</p>
    </li>
    <li>
      <h3>Print and Design Services</h3>
      <p>Business Cards, Flyers, Brochures, Posters, Banners etc.</p>
    </li>
    <li>
      <h3>Photo Prints</h3>
      <p>HD Metal prints to photographic paper print</p>
    </li>
  </ul>

  <div class="back__marks">
    <span></span>
    <div class="social"><span class="social__dot"></span><span class="social__handle">inkoraprints</span></div>
    <div class="brand"><span class="brand__dot"></span><span class="brand__name">Inkora</span></div>
    <div class="social"><span class="social__dot"></span><span class="social__handle">inkora</span></div>
  </div>
</section>

</body>
</html>
```